Web Design Project - Quiet Harbor Advisors

I have a requirement for a simple website that I can manage and change content myself. I'd like to be able to include and change images frequently.

I run a small consulting firm and focus on the area of small to medium sized business turn around. The premise of the business service is that most small businesses "have a monkey on their back" - a problem they need to solve - for example "a Sales Monkey" where their sales team didn't have a solid process or approach or training or the right people; or "a Finance Monkey" where they needed help with Cash flow management or funding, or "an IT Monkey" where their IT systems aren't supporting their supply chain process or ordering process.

So the whole business is build around building monkey characters to represent specific business problems - thus the name Quiet Harbor Advisors.

This always builds into giving each employee their own Monkey character - mine is an Orangutan and appears on my card and Deon (who is our Lawyer) is a Baboon and his character is on his card. I'd like to see these characters also integrated into the site.

The site need to be pretty simple at this stage:

1. Home Page
2. Services Page
3. Who we are / team page
4. Contact Us page

Due to the nature of the name and the imagery around the business I'd like the site to be engaging and colourful, the language I'll use is accessible, down to earth and customer/solution focused.

Target Market(s)

Small to medium sized enterprises looking for assistance with their business. They will be looking for practical solutions at value for money pricing

Industry/Entity Type

Business Service

Requirements
Nice to have
• I'd like the monkey in the logo to swing.

On the People or team page - each person is to have their own monkey character - for example - my business card shows my monkey character as an Orangutan and Deon's monkey character is a baboon - so as the business grows each new person gets their own monkeys character. So on the people or team page it would be fun to have some kind of jungle scene with the character monkeys placed in there and some descriptor of the person.

```html
<!DOCTYPE html>
<html lang="en">
<head>
<meta charset="utf-8">
<title>Quiet Harbor Advisors</title>
<link rel="stylesheet" href="https://fonts.googleapis.com/css2?family=Mulish:wght@300;400;600;700;800&family=Ubuntu:wght@400;500;700&display=swap">
<style>
:root{
  --yellow:#dcc400;
  --yellow-deep:#c7ad00;
  --yellow-light:#e4cf12;
  --brown:#6a4708;
  --brown-dark:#4a3708;
  --ink:#3b3b3b;
  --text:#555;
  --rule:#e6e6e6;
  --page:#e8e8e8;
  --white:#fff;
  --btn-top:#f7e64a;
  --btn-bot:#e2c500;
}
*{box-sizing:border-box;margin:0;padding:0}
html,body{width:897px;height:1200px;overflow:hidden}
body{position:relative;background:var(--page);font-family:"Ubuntu",sans-serif;color:var(--text)}
.hero-band{position:absolute;left:0;top:0;width:897px;height:387px;background:var(--yellow-deep)}
.hero-column{position:absolute;left:60px;top:0;width:777px;height:387px;background:var(--yellow)}
.hero-art{position:absolute;left:460px;top:30px;width:360px;height:357px;border-radius:46% 46% 10% 10%;background:radial-gradient(ellipse at 45% 35%,rgba(255,245,150,.35),rgba(255,245,150,0) 70%)}
.site-nav{position:absolute;left:107px;top:29px;width:682px;height:48px;background:var(--white);box-shadow:0 1px 3px rgba(0,0,0,.25);display:flex;align-items:center}
.brand{width:226px;height:48px;display:flex;align-items:center;gap:8px;padding-left:12px;font-family:"Mulish",sans-serif;font-weight:700;font-size:16px;color:var(--brown)}
.brand-dot{width:12px;height:12px;border-radius:50%;background:var(--yellow)}
.nav-item{height:48px;display:flex;align-items:center;justify-content:center;border-left:1px solid var(--rule);font-size:10px;color:#444}
.nav-item.active{font-weight:700;color:var(--brown)}
.social{display:flex;gap:8px;padding-left:14px;border-left:1px solid var(--rule);height:48px;align-items:center}
.social span{width:18px;height:18px;background:var(--brown);border-radius:3px}
.social span.wide{width:30px}
.hero-kicker{position:absolute;left:123px;top:113px;font-family:"Mulish",sans-serif;font-weight:400;font-size:27px;color:var(--brown-dark)}
.hero-title{position:absolute;left:123px;top:143px;font-family:"Mulish",sans-serif;font-weight:800;font-size:28px;line-height:31px;color:var(--brown-dark)}
.hero-copy{position:absolute;left:123px;top:238px;width:300px;font-size:9.5px;line-height:12px;color:#7a6508}
.hero-cta{position:absolute;left:120px;top:317px;width:194px;height:38px;border-radius:19px;background:linear-gradient(#9a6512,#6e4306);color:var(--white);font-family:"Mulish",sans-serif;font-weight:700;font-size:17px;display:flex;align-items:center;justify-content:center;box-shadow:0 2px 3px rgba(0,0,0,.25)}
.content{position:absolute;left:60px;top:387px;width:777px;height:784px;background:var(--white)}
.section-rule{position:absolute;left:0;width:777px;height:1px;background:var(--rule)}
.section-title{position:absolute;left:0;width:777px;text-align:center;font-family:"Mulish",sans-serif;font-weight:700;font-size:17px;color:var(--ink)}
.service{position:absolute;width:220px;text-align:center}
.service h3{font-family:"Mulish",sans-serif;font-weight:700;font-size:17px;color:var(--ink)}
.service svg{display:block;margin:12px auto 0}
.service h4{font-family:"Mulish",sans-serif;font-weight:300;font-size:17px;color:#333;margin-top:10px}
.service p{font-size:9.5px;line-height:12px;color:#444;margin-top:3px}
.btn-more{display:flex;align-items:center;justify-content:center;width:70px;height:19px;border-radius:10px;background:linear-gradient(var(--btn-top),var(--btn-bot));border:1px solid #c9ad00;font-size:9.5px;color:#5a4500;margin:0 auto}
.why-copy{position:absolute;left:33px;top:297px;width:711px;text-align:center;font-size:9.5px;line-height:13px;color:#444}
.carousel-arrow{position:absolute;top:473px;width:14px;height:20px;background:var(--btn-bot);border:1px solid #c9ad00}
.client{position:absolute;top:458px;width:47px;height:47px;background:linear-gradient(#9a9a9a,#3e3e3e);border:1px solid #ccc}
.client.current{border:3px solid var(--yellow)}
.testimonial{position:absolute;left:0;top:522px;width:777px;text-align:center;font-size:9px;line-height:13px;color:#444;white-space:nowrap}
.quote-mark{position:absolute;font-family:"Mulish",sans-serif;font-size:26px;line-height:26px;font-weight:700;color:#bbb}
.client-name{position:absolute;left:0;top:559px;width:777px;text-align:center;font-size:10.5px;font-weight:700;color:#333}
.contact-line{position:absolute;left:0;width:777px;text-align:center;font-size:9.5px;color:#444}
.contact-line b{color:#222}
.signup{position:absolute;left:277px;top:741px;width:224px;height:20px;border:1px solid #d5d5d5;border-radius:10px;background:var(--white)}
.signup span{position:absolute;left:14px;top:4px;font-size:8.5px;color:#999}
.signup-btn{position:absolute;right:-1px;top:-1px;width:70px;height:20px;border-radius:10px;background:linear-gradient(var(--btn-top),var(--btn-bot));border:1px solid #c9ad00;font-size:10px;color:#4a3a00;display:flex;align-items:center;justify-content:center}
.copyright{position:absolute;left:0;top:1179px;width:897px;text-align:center;font-size:9.5px;color:#444}
</style>
</head>
<body>
<header>
  <div class="hero-band"></div>
  <div class="hero-column"></div>
  <div class="hero-art" role="img" aria-label="Faint line illustration of a cheerful monkey character waving"></div>
  <nav class="site-nav">
    <div class="brand"><span class="brand-dot"></span>Quiet Harbor Advisors</div>
    <div class="nav-item active" style="width:64px">Home</div>
    <div class="nav-item" style="width:67px">Services</div>
    <div class="nav-item" style="width:133px">Who we are / team page</div>
    <div class="nav-item" style="width:83px">Contact Us</div>
    <div class="social" aria-label="Social links"><span></span><span></span><span class="wide"></span></div>
  </nav>
  <p class="hero-kicker">you have monkey on your back</p>
  <h1 class="hero-title">Your any problem will be<br>Solved here!</h1>
  <p class="hero-copy">Ut wisi enim ad minim veniam, quis nostrud exerci tation ullamcorper suscipit lobortis nisl ut aliquip ex ea commodo consequat. Duis autem vel eum iriure dolor ...</p>
  <div class="hero-cta">Let us help you!</div>
</header>

<main class="content">
  <section>
    <div class="service" style="left:25px;top:32px">
      <h3>Sales Monkey?</h3>
      <svg width="52" height="52" viewBox="0 0 52 52"><circle cx="26" cy="26" r="23" fill="none" stroke="#8a8a8a" stroke-width="3"/><path d="M26 26V3A23 23 0 0 1 49 26Z" fill="#8a8a8a"/></svg>
      <h4>liber tempor</h4>
      <p>lectorum. Mirum est notare quam littera<br>gothica, quam nunc putamus</p>
      <div class="btn-more" style="margin-top:14px">More</div>
    </div>
    <div class="service" style="left:278px;top:32px">
      <h3>Finance Monkey?</h3>
      <svg width="54" height="52" viewBox="0 0 54 52"><rect x="2" y="4" width="7" height="44" fill="#8a8a8a"/><rect x="12" y="16" width="7" height="32" fill="#8a8a8a"/><rect x="22" y="24" width="7" height="24" fill="#8a8a8a"/><rect x="32" y="32" width="7" height="16" fill="#8a8a8a"/><rect x="0" y="48" width="54" height="3" fill="#8a8a8a"/></svg>
      <h4>liber tempor</h4>
      <p>lectorum. Mirum est notare quam littera<br>gothica, quam nunc putamus</p>
      <div class="btn-more" style="margin-top:14px">More</div>
    </div>
    <div class="service" style="left:530px;top:32px">
      <h3>IT Monkey?</h3>
      <svg width="50" height="52" viewBox="0 0 50 52"><path d="M10 6C4 6 4 14 12 14" fill="none" stroke="#8a8a8a" stroke-width="2"/><rect x="12" y="10" width="26" height="40" rx="13" fill="none" stroke="#8a8a8a" stroke-width="3"/><path d="M12 26H38M25 10V26" stroke="#8a8a8a" stroke-width="2"/><rect x="23" y="14" width="4" height="8" rx="2" fill="#8a8a8a"/></svg>
      <h4 style="margin-top:4px">liber tempor</h4>
      <p>lectorum. Mirum est notare quam littera<br>gothica, quam nunc putamus</p>
      <div class="btn-more" style="margin-top:14px">More</div>
    </div>
  </section>

  <div class="section-rule" style="top:229px"></div>

  <section>
    <h2 class="section-title" style="top:252px">Why choose us?</h2>
    <p class="why-copy">Ut wisi enim ad minim veniam, quis nostrud exerci tation ullamcorper suscipit lobortis nisl ut aliquip ex ea commodo consequat. Duis autem vel eum iriure dolor in hendrerit in vulputate velit esse molestie consequat, vel illum dolore eu feugiat nulla facilisis at vero eros et accumsan et iusto odio dignissim qui blandit praesent luptatum zzril delenit augue duis dolore te feugait nulla facilisi. Nam liber tempor cum soluta nobis eleifend ...</p>
    <div class="btn-more" style="position:absolute;left:353px;top:352px">More</div>
  </section>

  <div class="section-rule" style="top:394px"></div>

  <section>
    <h2 class="section-title" style="top:416px">Happy Clients</h2>
    <div class="carousel-arrow" style="left:19px"><svg width="12" height="18" viewBox="0 0 12 18"><path d="M8 5L4 9L8 13Z" fill="#5a4500"/></svg></div>
    <div class="client" style="left:49px" role="img" aria-label="Client portrait photo"></div>
    <div class="client" style="left:107px" role="img" aria-label="Client portrait photo"></div>
    <div class="client" style="left:165px" role="img" aria-label="Client portrait photo"></div>
    <div class="client" style="left:223px" role="img" aria-label="Client portrait photo"></div>
    <div class="client" style="left:281px" role="img" aria-label="Client portrait photo"></div>
    <div class="client" style="left:339px" role="img" aria-label="Client portrait photo"></div>
    <div class="client" style="left:397px" role="img" aria-label="Client portrait photo"></div>
    <div class="client current" style="left:452px" role="img" aria-label="Selected client portrait photo"></div>
    <div class="client" style="left:513px" role="img" aria-label="Client portrait photo"></div>
    <div class="client" style="left:571px" role="img" aria-label="Client portrait photo"></div>
    <div class="client" style="left:629px" role="img" aria-label="Client portrait photo"></div>
    <div class="client" style="left:687px" role="img" aria-label="Client portrait photo"></div>
    <div class="carousel-arrow" style="left:745px"><svg width="12" height="18" viewBox="0 0 12 18"><path d="M4 5L8 9L4 13Z" fill="#5a4500"/></svg></div>
    <span class="quote-mark" style="left:62px;top:512px">&ldquo;</span>
    <p class="testimonial">Ut wisi enim ad minim veniam, quis nostrud exerci tation ullamcorper suscipit lobortis nisl ut aliquip ex ea commodo consequat. Duis autem vel eum<br>iriure dolor in hendrerit in vulputate velit esse molestie consequat, vel illum dolore eu feugiat nulla facilisis</p>
    <span class="quote-mark" style="left:614px;top:532px">&rdquo;</span>
    <p class="client-name">-alan reeve</p>
  </section>

  <div class="section-rule" style="top:588px"></div>

  <section>
    <h2 class="section-title" style="top:610px">Have a Question?</h2>
    <p class="contact-line" style="top:636px">Duis autem vel eum iriure dolor in hendrerit in vulputate velit esse molestie consequat, vel illum dolore eu feugiat nulla facilisis</p>
    <p class="contact-line" style="top:655px"><b>Call us at :</b> ABN 48 270 315 906</p>
    <p class="contact-line" style="top:672px"><b>Reach us at :</b> &nbsp;suite 204-18 Larch Lane, Bay Ridge NSW 2141 Australia</p>
    <p class="contact-line" style="top:690px"><b>Write us at :</b> hello@quietharboradvisors.example</p>
    <p class="contact-line" style="top:715px"><b>Connect with us :</b></p>
    <div class="signup"><span>Enter your email address</span><div class="signup-btn">Submit</div></div>
  </section>
</main>

<footer class="copyright">Copyright © 2013 Quiet Harbor Advisors.</footer>
</body>
</html>
```